Web design for consulting advisory business company

We need a web for our business consulting company. The web should transmit simplicity, innovation, trust, and solid knowledge of what we do. Inspirational webs to take a look are: https://brimlotte.com/ and http://varunexa.com.br. Use blue colors.

Target Market(s)

Private companies

Industry/Entity Type

Management Consulting

Number of Pages Required

5+ page

Font styles to use
Serif
Sans Serif

Colors
3176b5
3276b5
85abd2
85cae6
33a6d7
0592cd
ffffff
1b1b1b
474747

Requirements
Must have
• - use of blue
• - images
• - same version in different languages (portugueses and spanish)
Nice to have
• - white as background

```html
<!DOCTYPE html>
<html lang="pt">
<head>
<meta charset="utf-8">
<title>Veltrano Partners – Business Consulting Advisory</title>
<link href="https://fonts.googleapis.com/css2?family=Mulish:wght@400;600;700;800&family=Roboto:wght@400;500;700&display=swap" rel="stylesheet">
<style>
:root{
  --blue:#3176b5;
  --blue-deep:#1f5fa8;
  --blue-bright:#0592cd;
  --blue-soft:#85abd2;
  --ink:#1b1b1b;
  --text:#474747;
  --white:#ffffff;
  --grey-band:#efefef;
  --grey-line:#8c9097;
  --dark:#2a2a2a;
}
*{margin:0;padding:0;box-sizing:border-box}
html,body{width:1200px;height:4296px;overflow:hidden;background:var(--white)}
body{font-family:"Mulish",sans-serif;color:var(--text);position:relative}
.abs{position:absolute}
a{color:inherit;text-decoration:none}

/* header */
.site-header{position:absolute;top:0;left:0;width:1200px;height:95px;background:var(--white)}
.brand{position:absolute;left:157px;top:28px;display:flex;align-items:center;gap:10px;font-family:"Mulish",sans-serif;font-weight:800;font-size:20px;white-space:nowrap;color:var(--blue)}
.brand-mark{width:32px;height:32px;background:var(--blue)}
.main-nav{position:absolute;left:472px;top:38px;display:flex;gap:14px;font-size:15px;white-space:nowrap;color:var(--blue)}
.lang{position:absolute;left:1020px;top:38px;font-size:15px;font-weight:700;white-space:nowrap;color:var(--blue)}

/* hero */
.hero{position:absolute;top:95px;left:0;width:1200px;height:588px;overflow:hidden}
.hero-photo{position:absolute;inset:0;background:linear-gradient(180deg,#2b3240 0%,#4a4c58 35%,#6c5a5e 55%,#3a3c45 75%,#24272e 100%)}
.hero-play{position:absolute;left:565px;top:150px}
.hero-title{position:absolute;top:238px;width:100%;text-align:center;font-family:"Roboto",sans-serif;font-weight:700;font-size:50px;line-height:48px;color:var(--white)}
.hero-sub{position:absolute;top:345px;width:100%;text-align:center;font-family:"Roboto",sans-serif;font-size:24px;line-height:27px;color:var(--white)}
.hero-scroll{position:absolute;left:588px;top:430px}
.hero-curves{position:absolute;left:0;top:0}

/* about */
.about-photo{left:200px;top:773px;width:287px;height:257px;background:linear-gradient(135deg,#1e5aa0,#b9c4cf 60%,#334d78)}
.about-title{left:575px;top:774px;font-family:"Roboto",sans-serif;font-weight:500;font-size:38px;color:var(--ink)}
.about-text{left:575px;top:838px;width:450px;font-size:17px;line-height:29px;color:var(--text)}
.btn{position:absolute;display:flex;align-items:center;justify-content:center;gap:8px;border-radius:24px;font-family:"Roboto",sans-serif;font-weight:700;font-size:15px;color:var(--white)}
.btn-blue{background:var(--blue-deep)}
.btn-dark{background:var(--dark)}

/* services */
.services{position:absolute;top:1186px;left:0;width:1200px;height:555px;background:linear-gradient(180deg,#1d1f24,#33363c 55%,#23252a);overflow:hidden}
.section-title{position:absolute;width:100%;text-align:center;font-family:"Roboto",sans-serif;font-weight:500;font-size:36px}
.services .section-title{top:55px;color:var(--white)}
.service{position:absolute;top:160px;width:200px;text-align:center}
.service-icon{margin:0 auto;width:129px;height:129px}
.service-name{margin-top:14px;font-family:"Roboto",sans-serif;font-weight:700;font-size:18px;line-height:20px;color:var(--white)}
.service-desc{margin-top:8px;font-size:14px;line-height:20px;color:#d8d8d8}
.arrow-nav{position:absolute}

/* sectors */
.sectors-title{left:166px;top:1843px;font-family:"Roboto",sans-serif;font-weight:500;font-size:36px;color:var(--ink)}
.sector-list{position:absolute;list-style:none;font-weight:700;font-size:17px;line-height:35px;color:var(--ink)}
.sector-list li::before{content:"›";color:var(--blue-bright);font-weight:800;font-size:26px;margin-right:8px;vertical-align:-2px}
.sectors-art{left:687px;top:1776px}

/* cases */
.cases-title{top:2182px;color:var(--blue-deep)}
.cases-photo{left:0;top:2254px;width:596px;height:396px;background:linear-gradient(120deg,#dfe4ea,#9aa5b3 45%,#3a4250 80%,#5d6674)}
.cases-panel{position:absolute;left:596px;top:2254px;width:604px;height:396px;background:linear-gradient(135deg,#2f7ac8,#1f5ea8 70%,#1a4f90);overflow:hidden}
.case-title{position:absolute;left:63px;top:100px;width:440px;font-weight:700;font-size:22px;line-height:33px;color:var(--white)}
.case-text{position:absolute;left:63px;top:182px;width:420px;font-size:18px;line-height:27px;color:#b9d4ef}
.dots{position:absolute;left:68px;top:289px;display:flex;gap:8px}
.dots span{width:12px;height:12px;border-radius:50%;background:var(--white)}
.dots span.off{background:transparent;border:2px solid var(--white)}

/* ecosystem */
.eco-photo{left:0;top:2650px;width:1200px;height:530px;background:linear-gradient(180deg,#8d97a3,#c9ced4 40%,#5b6470 80%,#3c434c)}
.eco-card{position:absolute;left:158px;top:2764px;width:458px;height:286px;background:var(--white)}
.eco-title{position:absolute;left:54px;top:44px;font-weight:700;font-size:28px;color:var(--blue-deep)}
.eco-text{position:absolute;left:54px;top:96px;width:370px;font-size:17px;line-height:27px;color:var(--ink)}

/* team */
.team{position:absolute;top:3180px;left:0;width:1200px;height:463px;background:var(--grey-band)}
.team .section-title{top:56px;color:var(--blue-deep);font-size:33px}
.team-photo{position:absolute;left:249px;top:133px;width:230px;height:230px;border-radius:50%;background:radial-gradient(circle at 50% 40%,#d5dde6,#8ea2b8 70%,#6b8098)}
.team-name{position:absolute;left:515px;top:148px;font-family:"Roboto",sans-serif;font-weight:700;font-size:21px;letter-spacing:1px;color:var(--ink)}
.team-bio{position:absolute;left:515px;top:192px;width:470px;font-size:15px;line-height:25px;color:var(--text)}
.read-more{position:absolute;left:515px;top:336px;font-weight:800;font-size:15px;color:var(--blue-deep)}

/* contact */
.contact-title{left:183px;top:3730px;font-family:"Roboto",sans-serif;font-weight:500;font-size:34px;color:var(--ink)}
.office{position:absolute;left:183px;font-size:14px;line-height:20px;color:var(--text)}
.office strong{display:block;font-weight:400;font-size:17px;color:var(--text);margin-bottom:2px}
.contact-mail{left:183px;top:4045px;font-weight:700;font-size:15px;color:var(--blue-deep)}
.contact-panel{position:absolute;left:599px;top:3643px;width:601px;height:498px;background:linear-gradient(160deg,#2e6fd0,#1e4fb0 60%,#173f95)}
.field{position:absolute;left:88px;width:401px;height:42px;border:1px solid #9fc0ec;background:rgba(255,255,255,.08);font-size:16px;color:var(--white);padding:10px 18px}
.submit{position:absolute;left:88px;top:418px;width:161px;height:40px;background:var(--ink);color:var(--white);font-family:"Roboto",sans-serif;font-weight:700;font-size:17px;display:flex;align-items:center;justify-content:center}

/* footer */
.site-footer{position:absolute;top:4141px;left:0;width:1200px;height:155px;background:var(--grey-band)}
.footer-nav{position:absolute;left:180px;top:48px;display:flex;gap:16px;font-size:16px;color:var(--ink)}
.copyright{position:absolute;left:180px;top:82px;font-size:12px;color:var(--ink)}
.social{position:absolute;left:895px;top:47px;display:flex;gap:7px}
.social span{width:32px;height:32px;border-radius:50%;background:var(--blue-deep)}
</style>
</head>
<body>

<header class="site-header">
  <a class="brand" href="#"><span class="brand-mark"></span>VELTRANO PARTNERS</a>
  <nav class="main-nav"><a>Princípios</a><a>Expertise</a><a>Cases</a><a>Ecosistema</a><a>Equipe Sênior</a><a>Contato</a></nav>
  <div class="lang">SP ⌄</div>
</header>

<section class="hero">
  <div class="hero-photo" role="img" aria-label="City skyline at dusk with office towers"></div>
  <svg class="hero-play" width="70" height="70" viewBox="0 0 70 70"><circle cx="35" cy="35" r="32" fill="none" stroke="#fff" stroke-width="3"/><path d="M27 21 L50 35 L27 49 Z" fill="#fff"/></svg>
  <h1 class="hero-title">BUSINESS CONSULTING<br>ADVISORY</h1>
  <p class="hero-sub">Adaptamos a equipe e os esforços para o problema,<br>combinando recursos seniores</p>
  <svg class="hero-scroll" width="26" height="44" viewBox="0 0 26 44"><path d="M2 4 H24 M13 4 V38 M4 29 L13 39 L22 29" fill="none" stroke="#fff" stroke-width="2.5"/></svg>
  <svg class="hero-curves" width="1200" height="588" viewBox="0 0 1200 588">
    <path d="M560 588 C 860 560 1040 470 1200 415 L1200 455 C 1060 505 880 575 700 588 Z" fill="#8c9097"/>
    <path d="M610 588 C 900 560 1060 490 1200 450 L1200 515 C 1060 555 920 588 820 588 Z" fill="#1f5fa8"/>
    <path d="M760 588 C 980 578 1110 540 1200 512 L1200 588 Z" fill="#fff"/>
  </svg>
</section>

<div class="abs about-photo" role="img" aria-label="Office building seen through a blue framed square"></div>
<h2 class="abs about-title">ABOUT US</h2>
<p class="abs about-text">Adaptamos a equipe e os esforços para o problema, combinando recursos sêniores e especialistas do setor com fortes recursos analíticos para fornecer soluções sustentáveis. Ouvimos atentamente os nossos clientes e combinamos as nossas equipes com as suas necessidades. Se o escopo do projeto mudar,</p>
<a class="btn btn-blue" style="left:575px;top:1030px;width:187px;height:45px">LEARN MORE <span>→</span></a>

<section class="services">
  <svg class="abs" style="left:0;top:0" width="620" height="160" viewBox="0 0 620 160">
    <path d="M0 0 H600 C 380 8 180 40 0 110 Z" fill="#fff"/>
    <path d="M-10 118 C 170 45 380 12 600 4" fill="none" stroke="#8c9097" stroke-width="20"/>
    <path d="M-10 150 C 180 70 390 28 610 18" fill="none" stroke="#1f5fa8" stroke-width="26"/>
  </svg>
  <h2 class="section-title">SERVIÇO</h2>
  <svg class="arrow-nav" style="left:88px;top:262px" width="44" height="26" viewBox="0 0 44 26"><path d="M42 13 H4 M14 3 L3 13 L14 23" fill="none" stroke="#fff" stroke-width="2.5"/></svg>
  <svg class="arrow-nav" style="left:1064px;top:262px" width="44" height="26" viewBox="0 0 44 26"><path d="M2 13 H40 M30 3 L41 13 L30 23" fill="none" stroke="#fff" stroke-width="2.5"/></svg>

  <div class="service" style="left:150px">
    <svg class="service-icon" viewBox="0 0 129 129"><path d="M12 20 H117 V117 H12 Z" fill="#fff"/><path d="M4 12 H60 L4 60 Z" fill="#1f5fa8"/><rect x="30" y="38" width="69" height="62" fill="#1f5fa8"/><circle cx="64" cy="66" r="16" fill="none" stroke="#fff" stroke-width="4"/><circle cx="64" cy="66" r="5" fill="#fff"/></svg>
    <div class="service-name">Planejamento<br>Estratégico</div>
    <div class="service-desc">Pellentesque faucibus Ut accumsan ultricies elit</div>
  </div>
  <div class="service" style="left:388px">
    <svg class="service-icon" viewBox="0 0 129 129"><path d="M12 20 H117 V117 H12 Z" fill="#fff"/><path d="M4 12 H60 L4 60 Z" fill="#1f5fa8"/><rect x="30" y="38" width="69" height="62" fill="#1f5fa8"/><rect x="46" y="48" width="36" height="44" fill="none" stroke="#fff" stroke-width="4"/><path d="M56 58 H72 M56 68 H72 M56 78 H72" stroke="#fff" stroke-width="4"/></svg>
    <div class="service-name">Comercial</div>
    <div class="service-desc">Pellentesque faucibus Ut accumsan ultricies elit Maecenas at justo id velit placerat</div>
  </div>
  <div class="service" style="left:623px">
    <svg class="service-icon" viewBox="0 0 129 129"><path d="M12 20 H117 V117 H12 Z" fill="#fff"/><path d="M4 12 H60 L4 60 Z" fill="#1f5fa8"/><rect x="30" y="38" width="69" height="62" fill="#1f5fa8"/><circle cx="64" cy="69" r="17" fill="none" stroke="#fff" stroke-width="6" stroke-dasharray="6 4"/><circle cx="64" cy="69" r="7" fill="#fff"/></svg>
    <div class="service-name">Operações</div>
    <div class="service-desc">Pellentesque faucibus Ut accumsan ultricies elit Maecenas at justo id velit placerat</div>
  </div>
  <div class="service" style="left:869px">
    <svg class="service-icon" viewBox="0 0 129 129"><path d="M12 20 H117 V117 H12 Z" fill="#fff"/><path d="M4 12 H60 L4 60 Z" fill="#1f5fa8"/><rect x="30" y="38" width="69" height="62" fill="#1f5fa8"/><circle cx="50" cy="60" r="6" fill="#fff"/><circle cx="64" cy="56" r="7" fill="#fff"/><circle cx="78" cy="60" r="6" fill="#fff"/><path d="M40 90 V76 H88 V90" fill="none" stroke="#fff" stroke-width="4"/></svg>
    <div class="service-name">Pessoas &amp;<br>Organização</div>
    <div class="service-desc">Pellentesque faucibus Ut accumsan ultricies elit</div>
  </div>
  <a class="btn btn-blue" style="left:501px;top:452px;width:183px;height:45px">VIEW ALL <span>→</span></a>
</section>

<h2 class="abs sectors-title">SECTORS</h2>
<ul class="sector-list" style="left:172px;top:1916px">
  <li>Bens de Consumo</li><li>Varejo</li><li>Serviços Financeiros</li><li>Saúde</li><li>TelCo &amp; Mídia</li>
</ul>
<ul class="sector-list" style="left:398px;top:1916px">
  <li>Indústria</li><li>Esportes e Grandes Eventos</li><li>Transporte &amp; Logística</li><li>Energia &amp; Meio Ambiente</li><li>Private Equity</li>
</ul>
<svg class="abs sectors-art" width="367" height="372" viewBox="0 0 367 372" role="img" aria-label="Diamond frame filled with a photo of glass towers">
  <defs><linearGradient id="diamondFill" x1="0" y1="0" x2="0" y2="1"><stop offset="0" stop-color="#3a7fd0"/><stop offset=".55" stop-color="#c7d0da"/><stop offset="1" stop-color="#5c6673"/></linearGradient></defs>
  <path d="M183 4 L363 186 L183 368 L4 186 Z" fill="url(#diamondFill)"/>
</svg>

<h2 class="section-title cases-title">CASES</h2>
<div class="abs cases-photo" role="img" aria-label="Two businessmen reviewing documents at a laptop"></div>
<div class="cases-panel">
  <svg class="abs" style="left:0;top:0" width="604" height="200" viewBox="0 0 604 200">
    <path d="M300 -5 C 430 10 540 50 610 110" fill="none" stroke="#8c9097" stroke-width="22"/>
    <path d="M340 -10 C 460 0 560 30 620 70" fill="none" stroke="#b8bdc4" stroke-width="12"/>
  </svg>
  <h3 class="case-title">Desenvolvimento do orçamento anual e plano de investimento trienal</h3>
  <p class="case-text">para Grande Empresa Brasileira de Serviços Financeiros, identificando oportunidades de melhoria de 9% do orçamento total</p>
  <div class="dots"><span class="off"></span><span></span><span></span><span></span></div>
</div>

<div class="abs eco-photo" role="img" aria-label="Glass skyscrapers seen from below against a grey sky"></div>
<div class="eco-card">
  <h2 class="eco-title">ECOSISTEMA</h2>
  <p class="eco-text">Nos juntamos a especialistas globais e pioneiros de todo o mundo. A necessidade de velocidade e complexidade</p>
  <a class="btn btn-dark" style="left:54px;top:220px;width:186px;height:45px">LEARN MORE <span>→</span></a>
</div>

<section class="team">
  <h2 class="section-title">EQUIPE SÊNIOR</h2>
  <svg class="arrow-nav" style="left:118px;top:255px" width="46" height="28" viewBox="0 0 46 28"><path d="M44 14 H4 M15 3 L3 14 L15 25" fill="none" stroke="#1b1b1b" stroke-width="2.5"/></svg>
  <svg class="arrow-nav" style="left:1042px;top:255px" width="46" height="28" viewBox="0 0 46 28"><path d="M2 14 H42 M31 3 L43 14 L31 25" fill="none" stroke="#1b1b1b" stroke-width="2.5"/></svg>
  <div class="team-photo" role="img" aria-label="Portrait of a senior partner in a suit"></div>
  <h3 class="team-name">TOMÁS ELIZALDE</h3>
  <p class="team-bio">Administrador de Empresas pela Universidade Austral do Prata (ARG) e Master em Business Administration (MBA) pela Harlow Business School at the University of Eastbrook (EUA). Tem atuado como consultor de negócios nas áreas de planejamento estratégico, eficiência organizacional</p>
  <a class="read-more">READ MORE</a>
</section>

<h2 class="abs contact-title">CONTACT US</h2>
<div class="office" style="top:3797px;width:300px"><strong>Rio de Janeiro</strong>Av. das Palmeiras, 418 – 9º andar – Centro<br>Rio de Janeiro | 20040-112 | RJ</div>
<div class="office" style="top:3879px;width:320px"><strong>São Paulo</strong>Rua Aurora Lenz, 75 – Torre B, 3º andar – Vila Olímpia São Paulo | 04550-210 | SP</div>
<div class="office" style="top:3961px;width:320px"><strong>Buenos Aires</strong>Av. del Parque 1187 - Olivos Buenos Aires | B1636 KLM | Argentina</div>
<a class="abs contact-mail">contato@veltrano-partners.com.br</a>

<div class="contact-panel" role="img" aria-label="City towers tinted in blue">
  <div class="field" style="top:117px">Nome:</div>
  <div class="field" style="top:167px">Organização:</div>
  <div class="field" style="top:217px">Telefone:</div>
  <div class="field" style="top:267px">E-mail:</div>
  <div class="field" style="top:317px;height:72px">Mensagem:</div>
  <div class="submit">SUBMIT</div>
</div>

<footer class="site-footer">
  <nav class="footer-nav"><a>Princípios</a><a>Expertise</a><a>Cases</a><a>Ecosistema</a><a>Equipe Sênior</a><a>Contato</a></nav>
  <p class="copyright">© 2019 Company Name  All right reserved</p>
  <div class="social"><span></span><span></span><span></span><span></span></div>
</footer>

</body>
</html>
```